MOREVI VEGAN SUSHI

www.morevi-restaurant.de
We are open in 2018 and are an innovative restaurant from Munich. We would like a cool design for our drinks and food menu. It's very simple at the moment. See the File menu. In any case, our logo should appear. On the website we use neutraface as a font. But it's not a must. We are only open in the evening and appeal to a young, upscale audience.

```html
<!DOCTYPE html>
<html lang="de">
<head>
<meta charset="utf-8">
<title>MOREVI Vegan Sushi – Menu</title>
<link href="https://fonts.googleapis.com/css2?family=Josefin+Sans:ital,wght@0,400;0,600;0,700;1,400&display=swap" rel="stylesheet">
<style>
  :root {
    --stage: #8b8783;
    --paper: #ebe6de;
    --paper-dark: #ddd6cb;
    --ink: #1c1a18;
    --ink-soft: #3a3631;
    --rule: #2a2724;
    --photo-warm: #c98a6a;
    --photo-light: #d9cbb8;
    --photo-dark: #6b5a4a;
  }
  * { box-sizing: border-box; margin: 0; padding: 0; }
  html, body { width: 1200px; height: 1000px; overflow: hidden; }
  body {
    background: var(--stage);
    font-family: "Josefin Sans", "Helvetica Neue", Arial, sans-serif;
    color: var(--ink);
    position: relative;
  }
  .menu-card {
    position: absolute;
    left: 42px; top: 106px;
    width: 970px; height: 685px;
    transform: scale(1.15);
    transform-origin: top left;
    background: radial-gradient(ellipse at 40% 45%, var(--paper) 0%, var(--paper) 55%, var(--paper-dark) 100%);
    box-shadow: 0 6px 18px rgba(0,0,0,.35);
    overflow: hidden;
  }
  .menu-card__frame {
    position: absolute; inset: 4px;
    border: 1px solid var(--rule);
    pointer-events: none;
  }
  .photo {
    position: absolute;
  }
  .photo--platter {
    left: 212px; top: 188px; width: 480px; height: 480px;
    border-radius: 50%;
    background: radial-gradient(circle, rgba(107,90,74,.22) 0%, rgba(201,138,106,.18) 45%, rgba(217,203,184,.12) 75%, rgba(217,203,184,0) 100%);
  }
  .photo--rolls {
    left: 650px; top: 30px; width: 300px; height: 180px;
    background: radial-gradient(ellipse at 55% 50%, rgba(201,138,106,.55) 0%, rgba(217,203,184,.45) 55%, rgba(235,230,222,0) 80%);
  }
  .photo--nigiri {
    left: 115px; top: 555px; width: 170px; height: 110px;
    background: radial-gradient(ellipse at 50% 55%, rgba(190,90,70,.45) 0%, rgba(217,203,184,.25) 60%, rgba(235,230,222,0) 85%);
  }
  .brand-mark {
    position: absolute; top: 22px;
    width: 118px; height: 118px;
    border: 1px solid var(--ink-soft);
    border-radius: 50%;
    display: flex; align-items: center; justify-content: center;
    font-size: 15px; font-weight: 400; letter-spacing: 4px;
    color: var(--ink-soft);
  }
  .brand-mark--left { left: 74px; }
  .brand-mark--right { left: 776px; }
  .title-box {
    position: absolute; left: 286px; top: 35px;
    width: 376px; height: 92px;
    border: 1px solid var(--rule);
    text-align: center;
  }
  .title-box__heading {
    font-size: 60px; font-weight: 700; letter-spacing: 1px;
    line-height: 1; margin-top: 12px;
  }
  .title-box__sub {
    font-size: 16px; letter-spacing: 2.5px; margin-top: 1px;
  }
  .opening-hours {
    position: absolute; left: 0; width: 950px; top: 137px;
    text-align: center; font-size: 20px; letter-spacing: 2px;
  }
  .header-rule {
    position: absolute; left: 30px; top: 185px; width: 900px;
    border-top: 1px solid var(--rule);
  }
  .column-rule {
    position: absolute; top: 207px; height: 460px;
    border-left: 1px solid var(--rule);
  }
  .column-rule--a { left: 315px; }
  .column-rule--b { left: 678px; }
  .menu-column {
    position: absolute; top: 212px;
    font-size: 13px; line-height: 17.5px;
  }
  .menu-column--left { left: 31px; width: 268px; }
  .menu-column--middle { left: 351px; width: 288px; }
  .menu-column--right { left: 713px; width: 238px; }
  .menu-section + .menu-section { margin-top: 11px; }
  .menu-section__title,
  .menu-item {
    display: flex; justify-content: space-between; gap: 6px;
  }
  .menu-section__title {
    font-weight: 700; font-size: 13px; letter-spacing: .3px;
  }
  .menu-section__title small { font-weight: 400; font-size: 13px; }
  .menu-item { font-style: italic; }
  .menu-item .price, .menu-section__title .price {
    font-style: normal; font-weight: 400; white-space: nowrap;
  }
  .menu-column--right .menu-section + .menu-section { margin-top: 16px; }
  .vegan-note {
    position: absolute; left: 31px; top: 612px; width: 270px;
  }
  .vegan-note__label { font-weight: 700; font-size: 12px; }
  .vegan-note__text {
    font-style: italic; font-size: 8.5px; line-height: 11px; text-transform: uppercase;
  }
</style>
</head>
<body>
  <main class="menu-card">
    <div class="photo photo--platter" role="img" aria-label="Faint photo of a round sushi platter with assorted rolls and chopsticks"></div>
    <div class="photo photo--rolls" role="img" aria-label="Photo of a plate of vegan sushi rolls and nigiri"></div>
    <div class="photo photo--nigiri" role="img" aria-label="Photo of vegan nigiri pieces"></div>

    <div class="brand-mark brand-mark--left">MOREVI</div>
    <div class="brand-mark brand-mark--right">MOREVI</div>

    <header class="title-box">
      <h1 class="title-box__heading">MENU</h1>
      <p class="title-box__sub">FOOD &amp; DRINKS</p>
    </header>
    <p class="opening-hours">MON-SAT: 5.30PM-10PM</p>
    <div class="header-rule"></div>
    <div class="column-rule column-rule--a"></div>
    <div class="column-rule column-rule--b"></div>

    <section class="menu-column menu-column--left">
      <div class="menu-section">
        <h2 class="menu-section__title"><span>CHEF MENÜ MIT APERITIV</span><span class="price">81,00€</span></h2>
        <p class="menu-item"><span style="font-style:normal">(für 2 Personen)</span></p>
        <p class="menu-item"><span>Kleine Portion RAMENSUPPE<br>mit Gemüse &amp; Nudeln<br>MINI SET<br>DESSERT</span></p>
      </div>
      <div class="menu-section">
        <h2 class="menu-section__title"><span>OMAKASE <small>&nbsp;(für 2 Personen)</small></span><span class="price">68,00€</span></h2>
        <p class="menu-item"><span>EDAMAME<br>OMAKASE SET<br>mit 8 Spezialitäten des Hauses<br>PANA COTTA mit Beeren</span></p>
      </div>
      <div class="menu-section">
        <h2 class="menu-section__title"><span>HAUPTSPEISEN</span></h2>
        <p class="menu-item"><span>Herrlich cremiges KATSU CURRY<br>mit knusprigen Auberginensticks,<br>Reis &amp; Pickles</span><span class="price">17,90€</span></p>
        <p class="menu-item"><span>RAMEN SUPPE mit Nudeln,<br>Gemüse &amp; Tofu</span><span class="price">14,90€</span></p>
        <p class="menu-item"><span>CHIRASHI SUSHI BOWL</span><span class="price">13,90€</span></p>
        <p class="menu-item"><span>SOMMERSALATE mit Sesamdressing<br>&amp; crispy Tofusticks mit Mayo</span><span class="price">12,50€</span></p>
      </div>
    </section>

    <div class="vegan-note">
      <p class="vegan-note__label">*ALL VEGAN</p>
      <p class="vegan-note__text">Bitte teilen Sie dem Service unbedingt Allergien<br>mit und fragen Sie nach<br>der Allergiker-Menükarte.</p>
    </div>

    <section class="menu-column menu-column--middle">
      <div class="menu-section">
        <h2 class="menu-section__title"><span>VORSPEISEN</span></h2>
        <p class="menu-item"><span>MISO SUPPE 5,50€</span><span class="price">5,50€</span></p>
        <p class="menu-item"><span>EDAMAME MIT SALZ/CHILI 4,50€</span><span class="price">4,50€</span></p>
        <p class="menu-item"><span>SEIDENTOFU in hausgemachter Sauce<br>mit Mandeln 5,50€</span><span class="price">5,50€</span></p>
      </div>
      <div class="menu-section">
        <h2 class="menu-section__title"><span>SUSHI</span></h2>
        <p class="menu-item"><span>URAMAKI mit Tempuragemüse</span><span class="price">8,90€</span></p>
        <p class="menu-item"><span>FUTOMAKI wechselndes Gemüs</span><span class="price">8,00€</span></p>
        <p class="menu-item"><span>URAMAKI mit Austernpilze</span><span class="price">7,50€</span></p>
        <p class="menu-item"><span>HOSOMAKI Gurke Avocado</span><span class="price">5,50€</span></p>
        <p class="menu-item"><span>HOSOMAKI Gurke Shiitake</span><span class="price">5,50€</span></p>
        <p class="menu-item"><span>TOMATEN NIGIRI</span><span class="price">4,50€</span></p>
      </div>
      <div class="menu-section">
        <h2 class="menu-section__title"><span>KLEINE GERICHTE</span></h2>
        <p class="menu-item"><span>GEMÜSE TEMPURA</span><span class="price">8,00€</span></p>
        <p class="menu-item"><span>Crispy TOFUSTICKS mit Mayo</span><span class="price">8,00€</span></p>
        <p class="menu-item"><span>KÜRBISKROKETTEN mit TANGASHU</span><span class="price">7,90€</span></p>
        <p class="menu-item"><span>SUSHI “THUNA” CAKE</span><span class="price">6,90€</span></p>
        <p class="menu-item"><span>SUSHI CAKE CLASSIC</span><span class="price">6,00€</span></p>
        <p class="menu-item"><span>AUBERGINE DENGAKU</span><span class="price">5,00€</span></p>
      </div>
      <div class="menu-section">
        <h2 class="menu-section__title"><span>DESSERT</span></h2>
        <p class="menu-item"><span>CHEESECAKE mit Beeren</span><span class="price">6,50€</span></p>
        <p class="menu-item"><span>PANA COTTA mit Beeren</span><span class="price">5,90€</span></p>
        <p class="menu-item"><span>SORBET des Tages</span><span class="price">5,50€</span></p>
        <p class="menu-item"><span>SORBET des Tages mit Schuss</span><span class="price">6,90€</span></p>
      </div>
    </section>

    <section class="menu-column menu-column--right">
      <div class="menu-section">
        <h2 class="menu-section__title"><span>SET 1</span><span class="price">33,90€</span></h2>
        <p class="menu-item"><span>HOSOMAKI<br>FUTOMAKI<br>NIGIRI<br>KÜRBISKROKETTEN<br>WAKAME GURKEN SALAT<br>PICKLES<br>GYOZA TEIGTASCHEN<br>SUSHI CAKE</span></p>
      </div>
      <div class="menu-section">
        <h2 class="menu-section__title"><span>SET 2</span><span class="price">31,90€</span></h2>
        <p class="menu-item"><span>HOSOMAKI<br>FUTOMAKI<br>PICKLES<br>SUSHI “THUNA” CAKE<br>Crispy AUBERGINEN mit Mayo<br>AUBERGINE DENGAKU</span></p>
      </div>
      <div class="menu-section">
        <h2 class="menu-section__title"><span>SET 3</span><span class="price">28,90€</span></h2>
        <p class="menu-item"><span>HOSOMAKI<br>URAMAKI<br>NIGIRI<br>GEMÜSE TEMPURA<br>Crispy TOFUSTICKS mit Mayo<br>WAKAME SHIRA AE</span></p>
      </div>
    </section>

    <div class="menu-card__frame"></div>
  </main>
</body>
</html>
```